Financial Services Business Card Design

We are a financial services company Based in London, offering Short term Funding Solutions for companies, raising anywhere between £20,000 and £25million pounds.

The Card must have a professional look as it is going to be handed out to professionals I.E Solicitors, Accountants, Company directors and Business owners.

See Attached our company Logo

Industry/Entity Type

Business

Contact Information for Business Card

Lewis Thorncroft
Suite 41
R K House
Bramblecote Lane
Watford
HP19 4QX

```html
<!DOCTYPE html>
<html lang="en">
<head>
<meta charset="utf-8">
<title>Meridian Bridge Capital – Business Cards</title>
<link href="https://fonts.googleapis.com/css2?family=Open+Sans:wght@400;600;700&display=swap" rel="stylesheet">
<style>
  :root {
    --brand-blue: #1474bb;
    --brand-green: #238b3d;
    --accent-green: #3fb14f;
    --paper: #ffffff;
    --backdrop: #e9ebea;
    --ink: #4a4a4a;
    --rule: #cfcfcf;
  }
  * { box-sizing: border-box; margin: 0; padding: 0; }
  html, body { width: 1200px; height: 1064px; overflow: hidden; }
  body {
    background: var(--backdrop);
    font-family: "Open Sans", sans-serif;
    position: relative;
  }
  .card {
    position: absolute;
    width: 520px;
    height: 297px;
    border-radius: 3px;
    box-shadow: 0 6px 18px rgba(0,0,0,0.12);
    overflow: hidden;
  }
  .card--blue  { left: 60px;  top: 170px; background: var(--brand-blue); }
  .card--green { left: 620px; top: 170px; background: var(--brand-green); }
  .card--front { left: 60px;  top: 560px; background: var(--paper); }
  .card--details { left: 620px; top: 560px; background: var(--paper); }

  .wordmark {
    position: absolute;
    display: flex;
    align-items: center;
    gap: 12px;
    font-weight: 700;
    letter-spacing: 0.04em;
    text-transform: uppercase;
    line-height: 1.1;
  }
  .wordmark__dot {
    width: 16px; height: 16px; border-radius: 50%;
    background: currentColor; flex: none;
  }
  .card--blue .wordmark,
  .card--green .wordmark,
  .card--front .wordmark {
    left: 50%; top: 50%; transform: translate(-50%, -50%);
    font-size: 26px; white-space: nowrap;
  }
  .card--blue .wordmark,
  .card--green .wordmark { color: var(--paper); }
  .card--front .wordmark { color: var(--brand-blue); }

  .card--details .wordmark {
    left: 26px; top: 96px;
    font-size: 19px; color: var(--brand-blue);
    flex-wrap: nowrap;
  }
  .divider {
    position: absolute;
    left: 232px; top: 36px;
    width: 1px; height: 170px;
    background: var(--rule);
  }
  .contact {
    position: absolute;
    left: 252px; top: 34px;
    color: var(--ink);
    font-size: 11.5px;
    line-height: 1.5;
  }
  .contact__name {
    color: var(--brand-blue);
    font-weight: 700;
    font-size: 17px;
    line-height: 1.2;
  }
  .contact__title { font-size: 13px; margin-bottom: 8px; }
  .contact__address { margin-bottom: 8px; }
  .contact__row { display: flex; align-items: center; gap: 8px; }
  .contact__row svg { width: 12px; height: 12px; fill: var(--brand-blue); flex: none; }
  .band { position: absolute; left: 0; bottom: 0; width: 520px; height: 60px; }
</style>
</head>
<body>

  <section class="card card--blue" aria-label="Card back, blue">
    <div class="wordmark"><span class="wordmark__dot"></span>Meridian Bridge Capital</div>
  </section>

  <section class="card card--green" aria-label="Card back, green">
    <div class="wordmark"><span class="wordmark__dot"></span>Meridian Bridge Capital</div>
  </section>

  <section class="card card--front" aria-label="Card front, logo side">
    <div class="wordmark"><span class="wordmark__dot"></span>Meridian Bridge Capital</div>
  </section>

  <section class="card card--details" aria-label="Card front, contact side">
    <div class="wordmark"><span>Meridian Bridge<br>Capital</span></div>
    <div class="divider"></div>
    <div class="contact">
      <p class="contact__name">Lewis Thorncroft</p>
      <p class="contact__title">Your Title</p>
      <p class="contact__address">Suite 41, R K House<br>Bramblecote Lane, Watford HP19 4QX</p>
      <p class="contact__row">
        <svg viewBox="0 0 24 24" aria-hidden="true"><path d="M6.6 10.8a15.1 15.1 0 0 0 6.6 6.6l2.2-2.2a1 1 0 0 1 1-.25 11.4 11.4 0 0 0 3.6.57 1 1 0 0 1 1 1V20a1 1 0 0 1-1 1A17 17 0 0 1 3 4a1 1 0 0 1 1-1h3.5a1 1 0 0 1 1 1c0 1.25.2 2.45.57 3.57a1 1 0 0 1-.25 1z"/></svg>
        +44 020 7946 0831
      </p>
      <p class="contact__row">
        <svg viewBox="0 0 24 24" aria-hidden="true"><path d="M2 5h20v14H2z M3 6l9 7 9-7" fill="none" stroke="#1474bb" stroke-width="2"/></svg>
        info@meridianbridgecapital.com
      </p>
      <p class="contact__row">
        <svg viewBox="0 0 24 24" aria-hidden="true"><circle cx="12" cy="12" r="9" fill="none" stroke="#1474bb" stroke-width="2"/><path d="M3 12h18M12 3c3 3 3 15 0 18M12 3c-3 3-3 15 0 18" fill="none" stroke="#1474bb" stroke-width="1.6"/></svg>
        www.meridianbridgecapital.com
      </p>
    </div>
    <svg class="band" viewBox="0 0 520 60" preserveAspectRatio="none" aria-hidden="true">
      <polygon points="0,36 430,36 400,60 0,60" fill="var(--brand-blue)"/>
      <polygon points="430,36 520,36 520,60 400,60" fill="var(--accent-green)"/>
    </svg>
  </section>

</body>
</html>
```